Task and Project Management Tool Website

We need designs for both desktop and mobile for a new site, which is the marketing presentation of our new platform called Lanternfield, which is a task and project tool specific for the property sector. The name refers to people working on different workstreams on a property and crossing their paths when collaborating. The site will not do ecommerce, just a presentation of the product. We would like to include a video (no voice over) and some graphics, which we will do separately. The whole site will include a few pages, as detailed in the attach document. The product appeals to property companies and banks, hence the brand should portray reliability, corporate. We would like to see combinations of black, white and blue.
Updates

This project is currently put on hold. Client will be focusing on getting a Logo design first. Then once the logo has been created, we will resume this project and use the logo on the web designs submissions. Regards, QT Admin Barnaby

Logo design has been completed. Please resubmit and submit new web designs on this project using the logo design attached. Regards, QT Admin Barnaby

Target Market(s)

Corporate (B2B)

Logo Text

Lanternfield

Coding

Coded - Design and coding required

Number of Pages Required

5+ page

Requirements
Must have
• As in the specs
Should not have
• pictures of fake people (we prefer icons)

```html
<!DOCTYPE html>
<html lang="en">
<head>
<meta charset="utf-8">
<title>Lanternfield — Task and Project Management</title>
<link href="https://fonts.googleapis.com/css2?family=Montserrat:ital,wght@0,300;0,400;0,500;0,600;0,700;1,300;1,400&display=swap" rel="stylesheet">
<style>
:root{
  --blue:#2a9fd8;
  --blue-deep:#1b6fa8;
  --hero-a:#1f86c7;
  --hero-b:#2f9fd9;
  --ink:#1f2430;
  --navy:#1d2333;
  --text:#7b7f88;
  --muted:#a6a9b0;
  --line:#e6e8ec;
  --mist:#f2f4f7;
  --white:#ffffff;
}
*{margin:0;padding:0;box-sizing:border-box}
html,body{width:1200px;height:4451px;overflow:hidden}
body{position:relative;font-family:"Montserrat",sans-serif;color:var(--ink);background:var(--white)}
.abs{position:absolute}

/* hero */
.hero-bg{left:0;top:0;width:1200px;height:700px;background:linear-gradient(120deg,var(--hero-a),var(--hero-b) 55%,#1a78b8)}
.hero-wave{left:0;top:560px;width:1200px;height:160px}
.nav{left:0;top:36px;width:1200px;height:46px}
.brand{left:145px;top:6px;display:flex;align-items:center;gap:10px;color:var(--white);font-weight:700;font-size:26px;letter-spacing:.5px}
.brand i{display:block;width:22px;height:22px;background:var(--white)}
.menu{top:14px;font-size:14px;font-weight:500;color:var(--white);letter-spacing:.3px}
.pill{left:935px;top:4px;width:118px;height:38px;border-radius:19px;background:var(--white);color:var(--blue);font-size:12px;font-weight:700;display:flex;align-items:center;justify-content:center;letter-spacing:.3px}
.hero-title{left:0;width:1200px;top:160px;text-align:center;color:var(--white);font-size:66px;font-weight:700;letter-spacing:1px}
.hero-sub{left:0;width:1200px;top:264px;text-align:center;color:var(--white);font-size:18px;font-weight:500}
.btn{display:flex;align-items:center;justify-content:center;gap:8px;border-radius:23px;font-size:12px;font-weight:700;letter-spacing:.3px;height:45px}
.btn svg{width:11px;height:11px}
.btn-dark{left:444px;top:322px;width:149px;background:var(--navy);color:var(--white)}
.btn-line{left:605px;top:322px;width:151px;border:2px solid var(--white);color:var(--white)}
.dots{left:1122px;top:382px}
.dots span{display:block;width:8px;height:8px;border-radius:50%;background:var(--white);margin-bottom:10px}
.dots span.dim{opacity:.45}
.product{left:240px;top:455px;width:720px;height:427px;border-radius:14px;background:linear-gradient(180deg,#eef1f6,#dfe4ec);box-shadow:0 20px 40px rgba(20,40,70,.15)}

/* welcome */
.h2{font-size:39px;font-weight:700;letter-spacing:.5px}
.h2 b{color:var(--blue);font-weight:700}
.welcome{left:0;width:1200px;top:975px;text-align:center}
.lead{left:195px;width:810px;top:1058px;text-align:center;font-size:13.5px;line-height:30.5px;color:var(--text)}
.card{top:1252px;width:213px;height:174px;background:var(--white);border:1px solid var(--line);box-shadow:0 4px 12px rgba(0,0,0,.1);border-radius:3px;text-align:center}
.card svg{position:absolute;left:86px;top:38px;width:40px;height:40px}
.card p{position:absolute;left:0;width:100%;font-size:16px;font-weight:600;line-height:23px}

/* features */
.photo{background:linear-gradient(135deg,#9db7cf,#dfe8f1 55%,#6f8aa6)}
.ph-right{border-radius:0 80px 80px 0}
.ph-left{border-radius:80px 0 0 80px}
.feat-title{font-size:39px;font-weight:700;line-height:50px;letter-spacing:.5px}
.feat-title b{color:var(--blue)}
.copy{width:475px;font-size:13.5px;line-height:30.5px;color:var(--text)}
.btn-blue{width:151px;height:45px;background:var(--blue);color:var(--white);box-shadow:0 6px 12px rgba(42,159,216,.3)}
.rule{left:0;top:3323px;width:1200px;height:1px;background:var(--line)}

/* testimonials */
.quote{top:3546px;width:287px;height:180px;border:1px solid var(--line);box-shadow:0 2px 8px rgba(0,0,0,.05);padding:16px 20px}
.qhead{display:flex;align-items:center;gap:8px;color:var(--muted);font-size:22px;font-weight:700;line-height:20px}
.stars{color:#f5b400;font-size:12px;letter-spacing:1px}
.quote p{margin-top:12px;font-size:11.5px;font-style:italic;font-weight:300;line-height:22px;color:var(--muted)}
.person{top:3748px;display:flex;align-items:center;gap:14px}
.avatar{width:60px;height:60px;border-radius:50%;background:linear-gradient(135deg,#e7b98c,#8a5a3c)}
.person h4{font-size:13.5px;font-weight:600}
.person span{display:block;margin-top:4px;font-size:11.5px;color:var(--blue)}

/* contact */
.mist{left:0;top:3880px;width:1200px;height:360px}
.contact{top:4040px;width:260px;text-align:center}
.ring{margin:0 auto;width:72px;height:72px;border-radius:50%;border:2px solid #c9ccd2;background:var(--white);display:flex;align-items:center;justify-content:center}
.ring.fill{background:var(--blue);border-color:var(--blue)}
.ring svg{width:26px;height:26px}
.contact h5{margin-top:22px;font-size:15px;font-weight:700;letter-spacing:.3px}
.contact p{margin-top:8px;font-size:12px;line-height:22px;color:var(--text)}

/* footer */
.footer{left:0;top:4205px;width:1200px;height:246px}
.socials{left:0;width:1200px;top:4309px;display:flex;justify-content:center;gap:12px}
.socials span{width:40px;height:40px;border-radius:50%;border:2px solid var(--white);display:flex;align-items:center;justify-content:center}
.socials span i{width:12px;height:12px;border-radius:50%;background:var(--white)}
.fnav{left:0;width:1200px;top:4369px;display:flex;justify-content:center;gap:32px;color:var(--white);font-size:14px;font-weight:600}
.legal{left:0;width:1200px;top:4407px;text-align:center;color:var(--white);font-size:12px}
</style>
</head>
<body>

<!-- hero -->
<div class="abs hero-bg" role="img" aria-label="Blue-tinted photo of a team working together at a desk"></div>
<svg class="abs hero-wave" viewBox="0 0 1200 160" preserveAspectRatio="none"><path d="M0 100 C240 20 420 30 600 80 C800 135 1000 60 1200 40 L1200 160 L0 160 Z" fill="#ffffff"/></svg>

<header class="abs nav">
  <div class="abs brand"><i></i>LANTERNFIELD</div>
  <span class="abs menu" style="left:553px">HOME</span>
  <span class="abs menu" style="left:633px">ABOUT</span>
  <span class="abs menu" style="left:719px">SERVICES</span>
  <span class="abs menu" style="left:825px">CONTACT</span>
  <div class="abs pill">GET STARTED</div>
</header>

<h1 class="abs hero-title">LANTERNFIELD</h1>
<p class="abs hero-sub">At vero eos et accusamus et iusto odio dignissimos ducimus</p>
<div class="abs btn btn-dark">GET STARTED <svg viewBox="0 0 12 12"><circle cx="6" cy="6" r="6" fill="#fff"/><path d="M5 3.5 7.5 6 5 8.5" stroke="#1d2333" stroke-width="1.6" fill="none"/></svg></div>
<div class="abs btn btn-line">READ MORE <svg viewBox="0 0 12 12"><circle cx="6" cy="6" r="6" fill="#fff"/><path d="M5 3.5 7.5 6 5 8.5" stroke="#2a9fd8" stroke-width="1.6" fill="none"/></svg></div>
<div class="abs dots"><span></span><span class="dim"></span><span></span></div>

<div class="abs product" role="img" aria-label="Laptop showing the project dashboard with charts and task lists"></div>

<!-- welcome -->
<h2 class="abs h2 welcome">WELCOME TO <b>LANTERNFIELD</b></h2>
<p class="abs lead">Lorem ipsum dolor sit amet, consectetur adipiscing elit, sed do eiusmod tempor incididunt ut labore et dolore magna aliquaius ipsum suspendissgrs commodo viverra maecenas accumsan lacus vel facilisisLorem ipsum dolor sit amet, consectetur adipiscing elit, sed do eiusmod tempor incididunt ut labore et dolore magna aliquaius ipsum suspendissgrs commodo viverra maecenas accumsan lacus vel facilisis..</p>

<div class="abs card" style="left:145px">
  <svg viewBox="0 0 40 40" fill="#2a9fd8"><rect x="2" y="8" width="10" height="7" rx="1"/><rect x="15" y="8" width="10" height="7" rx="1"/><rect x="28" y="8" width="10" height="7" rx="1"/><rect x="2" y="17" width="10" height="7" rx="1"/><rect x="15" y="17" width="10" height="7" rx="1"/><rect x="28" y="17" width="10" height="7" rx="1"/><rect x="2" y="26" width="10" height="7" rx="1"/><rect x="15" y="26" width="10" height="7" rx="1"/><rect x="28" y="26" width="10" height="7" rx="1"/></svg>
  <p style="top:110px">OVERVIEW</p>
</div>
<div class="abs card" style="left:377px">
  <svg viewBox="0 0 40 40" fill="none" stroke="#2a9fd8" stroke-width="2.5"><path d="M20 6H6v28h28V20"/><path d="M30 4l6 6-14 14h-6v-6z"/></svg>
  <p style="top:98px">TASK<br>MANAGEMENT</p>
</div>
<div class="abs card" style="left:610px">
  <svg viewBox="0 0 40 40" fill="none" stroke="#2a9fd8" stroke-width="2.5"><rect x="3" y="6" width="34" height="22" rx="2"/><path d="M3 23h34M20 28v6M12 35h16"/></svg>
  <p style="top:110px">CRM</p>
</div>
<div class="abs card" style="left:842px">
  <svg viewBox="0 0 40 40" fill="none" stroke="#2a9fd8" stroke-width="2.5"><path d="M4 4v32h32"/><path d="M9 28l9-10 6 6 11-13"/><path d="M28 10h7v7"/></svg>
  <p style="top:98px">PROJECT<br>MANAGEMENT</p>
</div>

<!-- milestones -->
<div class="abs photo ph-right" style="left:0;top:1592px;width:503px;height:422px" role="img" aria-label="Two business people shaking hands in front of tall office windows"></div>
<h2 class="abs feat-title" style="left:568px;top:1606px">PROJECT <b>MILESTONES</b></h2>
<p class="abs copy" style="left:569px;top:1691px">Lorem ipsum dolor sit amet, consectetur adipiscing elit, sed do eiusmod tempor incididunt ut labore et dolore magna aliquaius ipsum suspendissgrs commodo viverra maecenas accumsan lacus vel facilisisLorem ipsum dolor sit amet, consectetur adipiscing elit, sed do eiusmod tempor incididunt ut labore et dolore magna aliquaius ipsum suspendissgrs commodo viverra maecenas accumsan lacus vel facilisis. .</p>
<div class="abs btn btn-blue" style="left:569px;top:1945px">READ MORE <svg viewBox="0 0 12 12"><circle cx="6" cy="6" r="6" fill="#fff"/><path d="M5 3.5 7.5 6 5 8.5" stroke="#2a9fd8" stroke-width="1.6" fill="none"/></svg></div>

<!-- track -->
<h2 class="abs feat-title" style="left:142px;top:2170px">TRACK PROJECTS<br><b>WITH EASE</b></h2>
<p class="abs copy" style="left:144px;top:2288px">Lorem ipsum dolor sit amet, consectetur adipiscing elit, sed do eiusmod tempor incididunt ut labore et dolore magna aliquaius ipsum suspendissgrs commodo viverra maecenas accumsan lacus vel facilisisLorem ipsum dolor sit amet, consectetur adipiscing elit, sed do eiusmod tempor incididunt ut labore et dolore magna aliquaius ipsum suspendissgrs commodo</p>
<div class="abs btn btn-blue" style="left:144px;top:2508px">READ MORE <svg viewBox="0 0 12 12"><circle cx="6" cy="6" r="6" fill="#fff"/><path d="M5 3.5 7.5 6 5 8.5" stroke="#2a9fd8" stroke-width="1.6" fill="none"/></svg></div>
<div class="abs photo ph-left" style="left:697px;top:2156px;width:503px;height:422px;background:linear-gradient(135deg,#8a5a36,#c79a6e 50%,#e9e6e2)" role="img" aria-label="Handshake over a wooden desk with a laptop, coffee and documents"></div>

<!-- portfolios -->
<div class="abs photo ph-right" style="left:0;top:2761px;width:503px;height:422px;background:linear-gradient(180deg,#5ea6df,#cfe3f2 45%,#6fb4c2 70%,#8c9a7a)" role="img" aria-label="Modern apartment buildings around a swimming pool"></div>
<h2 class="abs feat-title" style="left:568px;top:2775px">PROJECT <b>PORTFOLIOS</b></h2>
<p class="abs copy" style="left:569px;top:2860px">Lorem ipsum dolor sit amet, consectetur adipiscing elit, sed do eiusmod tempor incididunt ut labore et dolore magna aliquaius ipsum suspendissgrs commodo viverra maecenas accumsan lacus vel facilisisLorem ipsum dolor sit amet, consectetur adipiscing elit, sed do eiusmod tempor incididunt ut labore et dolore magna aliquaius ipsum suspendissgrs commodo viverra maecenas accumsan lacus vel facilisis. .</p>
<div class="abs btn btn-blue" style="left:569px;top:3113px">READ MORE <svg viewBox="0 0 12 12"><circle cx="6" cy="6" r="6" fill="#fff"/><path d="M5 3.5 7.5 6 5 8.5" stroke="#2a9fd8" stroke-width="1.6" fill="none"/></svg></div>

<div class="abs rule"></div>

<!-- testimonials -->
<h2 class="abs h2" style="left:0;width:1200px;top:3436px;text-align:center">WHAT CLIENTS <b>SAY</b></h2>

<div class="abs quote" style="left:137px"><div class="qhead">&ldquo;<span class="stars">★★★★★</span></div><p>Sed ut perspiciatis unde omnis iste natus error sit voluptatem accusantiuoloremque laudantium, totam rem aperiam, eaque ipsa quae ab illo inventore veritatis et qchitecto beatae vitae dicta sunt explicabo.</p></div>
<div class="abs quote" style="left:450px"><div class="qhead">&ldquo;<span class="stars">★★★★★</span></div><p>Sed ut perspiciatis unde omnis iste natus error sit voluptatem accusantiuoloremque laudantium, totam rem aperiam, eaque ipsa quae ab illo inventore veritatis et qchitecto beatae vitae dicta sunt explicabo.</p></div>
<div class="abs quote" style="left:761px"><div class="qhead">&ldquo;<span class="stars">★★★★★</span></div><p>Sed ut perspiciatis unde omnis iste natus error sit voluptatem accusantiuoloremque laudantium, totam rem aperiam, eaque ipsa quae ab illo inventore veritatis et qchitecto beatae vitae dicta sunt explicabo.</p></div>

<div class="abs person" style="left:148px"><div class="avatar" role="img" aria-label="Client portrait"></div><div><h4>Elton Marsh</h4><span>Posed on August 21, 2018</span></div></div>
<div class="abs person" style="left:460px"><div class="avatar" role="img" aria-label="Client portrait"></div><div><h4>Elton Marsh</h4><span>Posed on August 21, 2018</span></div></div>
<div class="abs person" style="left:771px"><div class="avatar" role="img" aria-label="Client portrait"></div><div><h4>Elton Marsh</h4><span>Posed on August 21, 2018</span></div></div>

<!-- contact -->
<svg class="abs mist" viewBox="0 0 1200 360" preserveAspectRatio="none">
  <path d="M0 60 C200 0 380 10 560 50 C760 95 980 30 1200 20 L1200 360 L0 360 Z" fill="#f3f5f8"/>
  <path d="M0 80 C260 30 460 60 640 90 C840 120 1020 70 1200 60 L1200 360 L0 360 Z" fill="#f8f9fb"/>
</svg>

<div class="abs contact" style="left:83px">
  <div class="ring"><svg viewBox="0 0 24 24" fill="#2a9fd8"><path d="M6.6 10.8c1.4 2.8 3.8 5.1 6.6 6.6l2.2-2.2c.3-.3.7-.4 1-.2 1.1.4 2.3.6 3.6.6.6 0 1 .4 1 1V20c0 .6-.4 1-1 1C10.6 21 3 13.4 3 4c0-.6.4-1 1-1h3.5c.6 0 1 .4 1 1 0 1.3.2 2.5.6 3.6.1.3 0 .7-.2 1z"/></svg></div>
  <h5>PHONE</h5><p>(+428) 555 010 2040</p>
</div>
<div class="abs contact" style="left:311px">
  <div class="ring"><svg viewBox="0 0 24 24" fill="#2a9fd8"><path d="M12 2a7 7 0 0 0-7 7c0 5.2 7 13 7 13s7-7.8 7-13a7 7 0 0 0-7-7zm0 9.5A2.5 2.5 0 1 1 12 6.5a2.5 2.5 0 0 1 0 5z"/></svg></div>
  <h5>HEAD OFFICE</h5><p>48 Harbour Lane, Old Quarter,<br>New State, USA, PO 4100</p>
</div>
<div class="abs contact" style="left:589px">
  <div class="ring fill"><svg viewBox="0 0 24 24" fill="#fff"><path d="M12 2a7 7 0 0 0-7 7c0 5.2 7 13 7 13s7-7.8 7-13a7 7 0 0 0-7-7zm0 9.5A2.5 2.5 0 1 1 12 6.5a2.5 2.5 0 0 1 0 5z"/></svg></div>
  <h5>MAIN OFFICE</h5><p>48 Harbour Lane, Old Quarter,<br>New State, USA, PO 4100</p>
</div>
<div class="abs contact" style="left:840px">
  <div class="ring"><svg viewBox="0 0 24 24" fill="#2a9fd8"><path d="M3 5h18v14H3z" opacity=".9"/><path d="M3 5l9 7 9-7" stroke="#fff" stroke-width="1.6" fill="none"/></svg></div>
  <h5>EMAIL</h5><p>hello@lanternfield.com</p>
</div>

<!-- footer -->
<svg class="abs footer" viewBox="0 0 1200 246" preserveAspectRatio="none"><path d="M0 0 L1200 70 L1200 246 L0 246 Z" fill="#1d2333"/></svg>
<div class="abs socials"><span><i></i></span><span><i></i></span><span><i></i></span><span><i></i></span><span><i></i></span></div>
<nav class="abs fnav"><span>HOME</span><span>ABOUT</span><span>SERVICES</span><span>CONTACT</span></nav>
<p class="abs legal">Copyrights © 2020, Lanternfield All rights reserved &nbsp;|&nbsp; Privacy policy &nbsp;|&nbsp; Site Map</p>

</body>
</html>
```